Meridian Sound Wellness LLC Card Design

Need business card with a logo for a hearing aid sales and audiology business. We have two Hearing Instrument Specialists and one Audiologist on staff. Over 25 years in business. Locally owned and operated. Financing available. Most insurances accepted.

Meridian Sound Wellness LLC
48730 W Linden Row, Suite 9
Spokane, WA 99481
509-617-2085
www.meridiansoundnorth.example

Manager
Tobias Wrenfield HIS COHC
License #81729046

Target Market(s)

50yr old + people with a hearing loss.

Industry/Entity Type

Business

Contact Information for Business Card

48730 W Linden Row, Suite 9
Spokane, WA 99481
509-617-2085
www.meridiansoundnorth.example

Manager
Tobias Wrenfield HIS COHC
NRPL #81729046

Font styles to use
Serif
Sans Serif

Requirements
Must have
• Business name, Tobias's name and title(s) and contact information, License #, web address
Nice to have
Should not have

```html
<!DOCTYPE html>
<html lang="en">
<head>
<meta charset="utf-8">
<title>Meridian Sound Wellness LLC – Business Card</title>
<link rel="stylesheet" href="https://fonts.googleapis.com/css2?family=Alegreya+Sans:ital,wght@0,400;0,500;1,400&family=Fira+Sans+Extra+Condensed:wght@700&display=swap">
<style>
  :root {
    --card-white: #ffffff;
    --brand-navy: #2b4fa3;
    --name-blue: #1b9ad8;
    --title-grey: #6a6a6a;
    --mark-green: #1f9a3a;
    --band-deep: #1a9ce2;
    --band-light: #a6dcf6;
    --ink: #1a1a1a;
  }
  * { margin: 0; padding: 0; box-sizing: border-box; }
  html, body {
    width: 1200px;
    height: 758px;
    overflow: hidden;
    background: var(--card-white);
  }
  .card {
    position: relative;
    width: 1200px;
    height: 758px;
    background: var(--card-white);
    font-family: "Alegreya Sans", "Segoe UI", sans-serif;
  }
  .brand-mark {
    position: absolute;
    left: 100px;
    top: 62px;
    width: 110px;
    height: 110px;
    border: 4px solid var(--mark-green);
    border-radius: 50%;
  }
  .company-name {
    position: absolute;
    left: 262px;
    top: 76px;
    width: 700px;
    font-family: "Fira Sans Extra Condensed", "Arial Narrow", sans-serif;
    font-weight: 700;
    font-size: 50px;
    line-height: 1;
    color: var(--brand-navy);
    white-space: nowrap;
  }
  .company-underglow {
    position: absolute;
    left: 270px;
    top: 138px;
    width: 680px;
    height: 26px;
    background: radial-gradient(ellipse at center, rgba(0,0,0,0.16) 0%, rgba(0,0,0,0.05) 45%, rgba(0,0,0,0) 70%);
  }
  .person {
    position: absolute;
    left: 0;
    top: 268px;
    width: 1200px;
    text-align: center;
  }
  .person-name {
    font-weight: 500;
    font-size: 50px;
    line-height: 1;
    color: var(--name-blue);
  }
  .person-role {
    margin-top: 4px;
    font-size: 44px;
    line-height: 1;
    color: var(--title-grey);
    font-variant: small-caps;
    letter-spacing: 1px;
  }
  .license {
    font-style: italic;
    font-size: 22px;
    font-variant: normal;
    letter-spacing: 0;
    vertical-align: 4px;
  }
  .contact {
    position: absolute;
    display: flex;
    align-items: center;
    color: var(--brand-navy);
    font-size: 32px;
    line-height: 1.3;
    font-variant: small-caps;
    font-weight: 500;
  }
  .contact svg { flex: none; fill: var(--brand-navy); }
  .contact-address { left: 116px; top: 492px; }
  .contact-address svg { margin-right: 14px; }
  .contact-phone { left: 746px; top: 516px; }
  .contact-phone svg { margin-right: 16px; }
  .web-band {
    position: absolute;
    left: 0;
    bottom: 0;
    width: 1200px;
    height: 134px;
    background: linear-gradient(to bottom, var(--band-deep) 0%, var(--band-light) 38%, var(--band-light) 62%, var(--band-deep) 100%);
    display: flex;
    align-items: center;
    justify-content: center;
  }
  .web-address {
    font-size: 36px;
    color: var(--ink);
  }
</style>
</head>
<body>
  <main class="card">
    <div class="brand-mark" aria-hidden="true"></div>
    <div class="company-underglow" aria-hidden="true"></div>
    <h1 class="company-name">Meridian Sound Wellness LLC</h1>

    <section class="person">
      <p class="person-name">Tobias Wrenfield HIS COHC</p>
      <p class="person-role">Manager <span class="license">(NRPL #81729046)</span></p>
    </section>

    <address class="contact contact-address">
      <svg width="50" height="46" viewBox="0 0 50 46" aria-hidden="true">
        <path d="M25 2 L48 22 L43 26 L25 10 L7 26 L2 22 Z"/>
        <path d="M10 26 L25 13 L40 26 V44 H30 V32 H20 V44 H10 Z"/>
      </svg>
      <span>48730 W Linden Row, Suite 9<br>Spokane, WA 99481</span>
    </address>

    <p class="contact contact-phone">
      <svg width="52" height="40" viewBox="0 0 52 40" aria-hidden="true">
        <path d="M2 12 C2 4 50 4 50 12 L50 16 L38 16 L38 11 C32 9 20 9 14 11 L14 16 L2 16 Z"/>
        <path d="M16 14 H36 L44 28 V38 H8 V28 Z"/>
        <g fill="#fff">
          <rect x="19" y="22" width="3" height="3"/><rect x="24.5" y="22" width="3" height="3"/><rect x="30" y="22" width="3" height="3"/>
          <rect x="19" y="27" width="3" height="3"/><rect x="24.5" y="27" width="3" height="3"/><rect x="30" y="27" width="3" height="3"/>
          <rect x="19" y="32" width="3" height="3"/><rect x="24.5" y="32" width="3" height="3"/><rect x="30" y="32" width="3" height="3"/>
        </g>
      </svg>
      <span>Tel: 509-617-2085</span>
    </p>

    <footer class="web-band">
      <p class="web-address">www.meridiansoundnorth.example</p>
    </footer>
  </main>
</body>
</html>
```